Harborline Bridal Bakery Selling Method needs finishing touches to website.

We have a temporary website located at http://www.brivantomarketworks.com/ql/.
We are doing a responsive design and have created the architecture (layout). However, we need a professional makeover for the graphic elements and colors of the website. The website will be selling a sales course to mostly women who sell wedding cakes.
The photos within the posted website are for illustrative purposes. We will use our own photos after the website is redone.
We are open to changing the font styles, borders, header, and anything else as long as the layout is not changed.
Target Market(s)
75% women age 25-50 and men 30-60.
Industry/Entity Type
Architecture
Colors
Designer to choose colors to be used in the design.
Look and feel
Each slider illustrates characteristics of the customer's brand and the style your logo design should communicate.

```html
<!DOCTYPE html>
<html lang="en">
<head>
<meta charset="utf-8">
<title>Harborline Bridal Bakery Selling Method</title>
<link rel="stylesheet" href="https://fonts.googleapis.com/css2?family=Gelasio:ital,wght@0,400;0,700;1,400;1,700&family=Open+Sans:wght@300;400&family=Tinos:wght@400;700&display=swap">
<style>
:root{
  --berry:#9a0a4a;
  --berry-deep:#6e0433;
  --berry-text:#8c0d47;
  --plum:#7a4a77;
  --ink:#222222;
  --ink-soft:#3a3a3a;
  --gold-top:#ffc43a;
  --gold-bottom:#f7a20b;
  --white:#ffffff;
  --rule:#dcdcdc;
  --night:#222326;
}
*{box-sizing:border-box;margin:0;padding:0}
html,body{width:686px;height:1200px;overflow:hidden;background:var(--white)}
body{position:relative;font-family:"Gelasio",Georgia,serif;color:var(--ink)}
.abs{position:absolute}

/* top banner */
.code-banner{left:134px;top:0;width:416px;height:51px;background:var(--berry);
  color:var(--white);font-style:italic;font-weight:700;font-size:15px;
  display:flex;align-items:center;justify-content:center;letter-spacing:.2px}

/* hero */
.hero-art{left:0;top:51px;width:686px;height:415px;
  background:
   radial-gradient(ellipse 160px 120px at 290px 70px,#3a0a1c 0%,rgba(58,10,28,0) 100%),
   radial-gradient(ellipse 260px 220px at 230px 330px,#c21a63 0%,rgba(194,26,99,0) 100%),
   radial-gradient(ellipse 200px 180px at 560px 80px,#b01458 0%,rgba(176,20,88,0) 100%),
   linear-gradient(160deg,#e79ac0 0%,#db6ea3 45%,#e7a3c4 100%)}
.main-nav{left:0;top:51px;width:686px;height:54px;background:rgba(150,150,150,.55);
  display:flex;align-items:center;font-family:"Tinos","Times New Roman",serif;
  font-size:14px;color:var(--white);text-transform:uppercase}
.main-nav a{position:absolute;color:var(--white);text-decoration:none;top:0;height:54px;
  display:flex;align-items:center}
.main-nav .is-current{left:0;width:104px;justify-content:center;background:var(--berry)}
.video-frame{left:27px;top:131px;width:399px;height:255px;background:rgba(20,12,16,.82);
  display:flex;align-items:center;justify-content:center;color:var(--white);
  font-style:italic;font-weight:700;font-size:14px}
.signup{left:444px;top:131px;width:224px;height:308px;
  background:linear-gradient(180deg,var(--berry) 0%,var(--berry-deep) 100%);color:var(--white)}
.signup h2{position:absolute;left:17px;top:14px;font-style:italic;font-weight:700;font-size:23px}
.signup p{position:absolute;left:17px;top:47px;width:205px;font-style:italic;font-size:19px;line-height:24px}
.signup .field{position:absolute;left:30px;width:166px;height:29px;background:var(--white);
  color:#8a8a8a;font-style:italic;font-weight:700;font-size:14px;padding:6px 10px}
.signup .field-name{top:163px}
.signup .field-email{top:200px}
.signup .cta{position:absolute;left:35px;top:247px;width:157px;height:40px;border-radius:6px;
  background:linear-gradient(180deg,var(--gold-top),var(--gold-bottom));color:#2a1a00;
  font-style:italic;font-weight:700;font-size:14px;display:flex;align-items:center;justify-content:center}

/* strip */
.tagline{left:0;top:466px;width:686px;height:29px;background:var(--white);color:var(--berry-text);
  font-style:italic;font-weight:700;font-size:14.5px;display:flex;align-items:center;justify-content:center}

/* showcase */
.showcase-art{left:0;top:495px;width:686px;height:302px;
  background:radial-gradient(ellipse 220px 90px at 350px 60px,#7d7d7d 0%,rgba(125,125,125,0) 100%),
  linear-gradient(180deg,#b9b9b9,#c9c9c9)}
.tile{top:582px;width:161px;height:215px}
.tile-sea{left:22px;background:linear-gradient(180deg,#cfcfcf 0%,#9a9a9a 55%,#6f6f6f 100%)}
.tile-note{left:183px;background:var(--plum);color:var(--white);text-align:center;padding-top:11px}
.tile-note h3{font-family:"Tinos","Times New Roman",serif;font-size:17px;font-weight:700}
.tile-note h4{font-family:"Tinos","Times New Roman",serif;font-size:12px;font-weight:700;margin-top:2px}
.tile-note p{font-family:"Tinos","Times New Roman",serif;font-size:7px;line-height:9.5px;
  margin:26px auto 0;width:134px}
.tile-model{left:344px;background:linear-gradient(180deg,#e3e3e3 0%,#cdcdcd 40%,#2e2e2e 100%)}
.tile-sign{left:505px;width:162px;background:linear-gradient(180deg,#dfe8f3,#c9d6ea)}

/* feature cards */
.features{left:0;top:797px;width:686px;height:303px;background:var(--white);border-left:1px solid var(--rule)}
.feature{position:absolute;top:25px;width:152px}
.feature h3{font-style:italic;font-weight:700;font-size:14.5px;line-height:17.3px;color:var(--ink-soft)}
.feature p{font-family:"Open Sans",Arial,sans-serif;font-weight:300;font-size:12.4px;line-height:17px;
  margin-top:17px;color:var(--ink)}
.feature .more{position:absolute;top:223px;width:106px;height:36px;
  background:linear-gradient(180deg,var(--berry),var(--berry-deep));color:var(--white);
  font-style:italic;font-weight:700;font-size:14px;display:flex;align-items:center;justify-content:center;
  box-shadow:0 1px 2px rgba(0,0,0,.35)}

/* footer */
.footer-fade{left:0;top:1100px;width:686px;height:72px;
  background:radial-gradient(ellipse 420px 70px at 343px 20px,#f7f7f7 0%,#e2e2e2 100%)}
.footer-base{left:0;top:1172px;width:686px;height:28px;background:var(--night)}
</style>
</head>
<body>

<header>
  <div class="abs code-banner">“SECRET CODE” BANNER</div>
</header>

<section aria-label="Hero">
  <div class="abs hero-art" role="img" aria-label="Close-up photograph of a wedding cake detail in pink and deep red tones"></div>
  <nav class="abs main-nav">
    <a class="is-current" href="#">Home</a>
    <a href="#" style="left:123px">Who is Len Varro?</a>
    <a href="#" style="left:300px">Why is Len sharing his secrets</a>
    <a href="#" style="left:585px">Contact</a>
  </nav>
  <div class="abs video-frame">VIDEO PLACEHOLDER</div>
  <form class="abs signup">
    <h2>FREE Videos</h2>
    <p>To Help You Sell More Wedding Cakes At Higher Prices... Immediately!</p>
    <div class="field field-name">Name</div>
    <div class="field field-email">Email</div>
    <div class="cta">Get instant access</div>
  </form>
</section>

<div class="abs tagline">3 Leading-Edge Techniques for Convincing Brides to Choose You</div>

<section aria-label="Showcase">
  <div class="abs showcase-art" role="img" aria-label="Grayscale photograph of a leafy tree"></div>
  <div class="abs tile tile-sea" role="img" aria-label="Black and white seaside photograph with a brand title"></div>
  <div class="abs tile tile-note">
    <h3>Lorem ipsum</h3>
    <h4>dolor sit amet</h4>
    <p>Consectetur adipiscing elit, sit amet et un faq lorem ipsum et amet. Lorem ipsum dolor sit amet consectetur adipis elit, sit amet et un faq lorem ipsum et amet. Lorem ipsum sit amet consectetur adipiscing elit, sit amet et un faq.</p>
  </div>
  <div class="abs tile tile-model" role="img" aria-label="Fashion photograph of a man in a dark shirt with a price tag"></div>
  <div class="abs tile tile-sign" role="img" aria-label="Photograph of a striped shop sign"></div>
</section>

<section class="abs features" aria-label="Video lessons">
  <article class="feature" style="left:33px">
    <h3>In the first video, discover a sales growth secret that reveals the "Two Faces Of Your Wedding Cake Business."</h3>
    <p>One side of your face displays your "Internal Reality." It's how you run your business. Whether.</p>
    <a class="more" style="left:14px">Read more</a>
  </article>
  <article class="feature" style="left:193px">
    <h3>In the first video, discover a sales growth secret that reveals the "Two Faces Of Your Wedding Cake Business."</h3>
    <p>One side of your face displays your "Internal Reality." It's how you run your business. Whether.</p>
    <a class="more" style="left:14px">Read more</a>
  </article>
  <article class="feature" style="left:353px">
    <h3>In the first video, discover a sales growth secret that reveals the "Two Faces Of Your Wedding Cake Business."</h3>
    <p>One side of your face displays your "Internal Reality." It's how you run your business. Whether.</p>
    <a class="more" style="left:14px">Read more</a>
  </article>
  <article class="feature" style="left:519px">
    <h3>In the first video, discover a sales growth secret that reveals the "Two Faces Of Your Wedding Cake Business."</h3>
    <p>One side of your face displays your "Internal Reality." It's how you run your business. Whether.</p>
    <a class="more" style="left:14px">Read more</a>
  </article>
</section>

<footer>
  <div class="abs footer-fade"></div>
  <div class="abs footer-base"></div>
</footer>

</body>
</html>
```